Flyer-Design für Vorstellung einer Maschine
Zielgruppe
Wir sind Maschinenbauer, und spezialisiert auf das Laserschweißen von Kunststoffen.
Aufgabenstellung
Es soll widergespiegelt werden, dass wir ein Technik-Unternehmen sind.
Bei diesem Flyer, der vorne und hinten bedruckt werden soll, geht es um die Vorstellung einer Maschine.
Der Informationscharakter steht im Vordergrund.

```html
<!DOCTYPE html>
<html lang="de">
<head>
<meta charset="utf-8">
<title>NXL 540 – Technische Daten</title>
<link href="https://fonts.googleapis.com/css2?family=Didact+Gothic&family=Share+Tech&display=swap" rel="stylesheet">
<style>
  :root {
    --navy-deep: #0a1f4f;
    --navy: #074483;
    --ink: #1b1b24;
    --tan: #b3a797;
    --row: #e6e1dc;
    --paper: #ffffff;
  }
  html, body { margin: 0; padding: 0; overflow: hidden; }
  body { width: 848px; height: 1200px; background: var(--paper); }
  .sheet {
    position: relative; width: 848px; height: 1200px; overflow: hidden;
    font-family: "Didact Gothic", sans-serif; color: var(--ink);
  }
  .brand-name {
    position: absolute; right: 58px; top: 58px;
    font-family: "Didact Gothic", sans-serif; font-size: 40px; letter-spacing: 5px;
    line-height: 48px; color: var(--navy-deep);
  }
  .title {
    position: absolute; left: 51px; top: 156px; margin: 0;
    font-family: "Share Tech", sans-serif; font-weight: 400; font-size: 30px;
    letter-spacing: 0.5px; color: var(--navy-deep);
  }
  .band { position: absolute; left: 0; top: 0; }
  .intro {
    position: absolute; left: 51px; top: 242px; width: 495px; margin: 0;
    color: #fff; font-size: 15.2px; line-height: 22.6px;
  }
  .photo { position: absolute; }
  .photo-frame {
    position: absolute; right: -7px; bottom: -7px; width: 100%; height: 100%;
    border-right: 4px solid var(--tan); border-bottom: 4px solid var(--tan);
    box-sizing: border-box;
  }
  .photo-fill { position: absolute; inset: 0; background: var(--paper); }
  .photo-fill span { position: absolute; inset: 18px; border-radius: 4px; }
  .photo-pen { left: 51px; top: 386px; width: 173px; height: 151px; }
  .photo-pen span { background: linear-gradient(150deg, #fff 0%, #b9c0d8 45%, #8e99c0 60%, #fff 100%); }
  .photo-part-a { left: 295px; top: 345px; width: 193px; height: 153px; }
  .photo-part-b { left: 549px; top: 305px; width: 193px; height: 152px; }
  .photo-part-a span, .photo-part-b span {
    background: linear-gradient(135deg, #fff 0%, #ece7de 35%, #a08c73 70%, #fff 100%);
  }
  .specs {
    position: absolute; left: 51px; top: 635px; width: 745px;
    border-collapse: collapse; table-layout: fixed; font-size: 15.4px;
  }
  .specs td { padding: 0 6px; height: 36px; vertical-align: middle; }
  .specs col.label-col { width: 210px; }
  .specs tr:nth-child(odd) { background: var(--row); }
  .specs td.list { line-height: 22.6px; padding-top: 6px; padding-bottom: 6px; }
</style>
</head>
<body>
<div class="sheet">
  <svg class="band" width="848" height="1200" viewBox="0 0 848 1200" aria-hidden="true">
    <defs>
      <linearGradient id="bandGrad" x1="0" y1="0" x2="1" y2="0">
        <stop offset="0" stop-color="#07508f"/>
        <stop offset="1" stop-color="#0a1f4f"/>
      </linearGradient>
    </defs>
    <path d="M0 222 Q430 215 848 146 L848 226 Q600 300 0 431 Z" fill="url(#bandGrad)"/>
  </svg>

  <div class="brand-name">NEXOLAS</div>

  <h1 class="title">TECHNISCHE DATEN</h1>

  <p class="intro">Die NXL 540 besitzt ein Standardgehäuse. Alle Komponenten wie Laser, Steuereinheit und Rundschalttisch sind im Gehäuse integriert. Das System kann sowohl für das Kontur- als auch das Quasisimultanverfahren eingesetzt werden.</p>

  <div class="photo photo-pen">
    <div class="photo-frame"></div>
    <div class="photo-fill" role="img" aria-label="Foto eines lasergeschweißten Injektionsstifts mit Kappe"><span></span></div>
  </div>
  <div class="photo photo-part-a">
    <div class="photo-frame"></div>
    <div class="photo-fill" role="img" aria-label="Foto eines lasergeschweißten Kunststoffbauteils"><span></span></div>
  </div>
  <div class="photo photo-part-b">
    <div class="photo-frame"></div>
    <div class="photo-fill" role="img" aria-label="Foto eines weiteren Kunststoffbauteils"><span></span></div>
  </div>

  <table class="specs">
    <colgroup><col class="label-col"><col></colgroup>
    <tr><td>Laserklasse</td><td>1</td></tr>
    <tr><td>Laserleistung</td><td>bis 250W</td></tr>
    <tr><td>Laser-Wellenlänge</td><td>980nm – weitere Wellenlängen auf Anfrage</td></tr>
    <tr><td>Bearbeitungsfeld</td><td>180 x 180 mm²</td></tr>
    <tr><td>Elektrischer Anschluss</td><td>400V, 50-60Hz, max. 3kW</td></tr>
    <tr><td>Druckluft</td><td>4,5 bar bis 10 bar Druckluft gemäß DIN 8573-1 Klasse 1-4-1</td></tr>
    <tr><td>Abmessungen (BxTxH)</td><td>ca. 820 x 1.460 x 1.840 mm³</td></tr>
    <tr><td>Ausstattung</td><td class="list">Elektrischer 2-Stationen Rundschalttisch<br>Hochpräzisions-Wegmesssystem<br>Automatische Spannkraftregelung<br>Industrie-PC mit Multi-Language-HMI, touchoptimiert<br>Schnittstellen zum Datenaustausch<br>NexoWeld Prozesssoftware</td></tr>
    <tr><td>Optional</td><td class="list">Ausbringungserhöhung, Temperaturüberwachung, Kraftmesssystem,<br>Paket «automatische Bestückung», Werkzeugcodierung, Bauteilerkennung,<br>NIO-Box, Transformator</td></tr>
  </table>
</div>
</body>
</html>
```